KRWM new business card design

We need a business card design for our established business which is Australia wide however based in Melbourne. We are a young team of Financial Planners who specialize in Insurance and Basic super advice for people like us.

We are people who help our clients get things done in a timely and cost effective manner whilst having a good time and a laugh along the way.

We would like this to have a consistent feel with our new e-brochure which i have attached from a color and font perspective.

Industry/Entity Type

Business

Requirements
Must have
• We do not need specific address details rather just the states we are in:

VIC/NSW/QLD/TAS
Nice to have
• Curved edge to mate the brochure

```html
<!DOCTYPE html>
<html lang="en">
<head>
<meta charset="utf-8">
<title>KRWM business card concepts</title>
<link href="https://fonts.googleapis.com/css2?family=Arimo:wght@400;700&display=swap" rel="stylesheet">
<style>
  :root {
    --ink: #231f20;
    --ink-soft: #2e2a2b;
    --paper: #f3f3f3;
    --paper-shade: #e2e2e2;
    --green: #6cc24a;
    --green-bright: #4fe04f;
    --green-deep: #8dc63f;
    --grey-text: #8c8c8c;
    --stage: #f4f4f4;
  }
  * { margin: 0; padding: 0; box-sizing: border-box; }
  html, body {
    width: 1056px; height: 1200px; overflow: hidden;
    background: var(--stage);
    font-family: "Arimo", Arial, sans-serif;
  }
  .sheet { position: relative; width: 1056px; height: 1200px; }

  .card {
    position: absolute; width: 575px; height: 330px;
    overflow: hidden;
    box-shadow: 0 3px 10px rgba(0,0,0,0.18);
  }
  .card--one   { left: 112px; top: 82px; }
  .card--two   { left: 388px; top: 452px; }
  .card--three { left: 182px; top: 808px; }

  .card__shapes { position: absolute; inset: 0; width: 100%; height: 100%; }

  .brand {
    position: absolute; top: 58px; width: 208px;
    display: flex; flex-direction: column; align-items: center; gap: 26px;
  }
  .brand__mark { width: 74px; height: 74px; background: var(--green-deep); }
  .brand__name { font-weight: 700; font-size: 38px; letter-spacing: 1px; color: var(--ink); }
  .card--two .brand__name { color: #ffffff; }

  .regions {
    position: absolute; top: 40px; list-style: none;
    font-weight: 700; font-size: 21px; line-height: 27px; color: var(--grey-text);
  }
  .regions li::before { content: "›"; margin-right: 8px; font-size: 22px; }
  .email {
    position: absolute; top: 192px;
    font-size: 19px; font-weight: 700; color: var(--grey-text);
  }
  .email__at { font-weight: 400; margin-right: 4px; }

  .web {
    position: absolute; top: 0; height: 330px; width: 60px;
    display: flex; flex-direction: column; align-items: center; justify-content: flex-end;
    padding-bottom: 26px; gap: 14px;
  }
  .web__url {
    writing-mode: vertical-rl; transform: rotate(180deg);
    font-weight: 700; font-size: 19px; color: var(--ink); letter-spacing: 0.3px;
  }
  .web__icon { width: 16px; height: 16px; }
  .card--two .web__url { color: #ffffff; }
</style>
</head>
<body>
<main class="sheet">

  <!-- Concept one: light brand panel, dark contact panel -->
  <article class="card card--one">
    <svg class="card__shapes" viewBox="0 0 575 330" aria-hidden="true">
      <rect width="575" height="330" fill="var(--paper)"/>
      <rect width="42" height="330" fill="var(--ink-soft)"/>
      <path d="M490 0 H524 V200 Q522 312 330 330 H490 Z" fill="var(--green)"/>
      <path d="M258 0 H505 V190 Q505 300 360 330 H258 Z" fill="var(--ink)"/>
    </svg>
    <div class="brand" style="left:44px">
      <span class="brand__mark"></span>
      <span class="brand__name">KRWM</span>
    </div>
    <ul class="regions" style="left:272px">
      <li>Victoria</li><li>New South Wales</li><li>Queensland</li><li>Tasmania</li>
    </ul>
    <p class="email" style="left:270px"><span class="email__at">@</span>alex@krwm.com.au</p>
    <div class="web" style="left:520px">
      <span class="web__url">www.krwm.com.au</span>
      <svg class="web__icon" viewBox="0 0 16 16"><circle cx="8" cy="8" r="7" fill="none" stroke="var(--ink)" stroke-width="2"/><path d="M1 8 H15 M8 1 V15" stroke="var(--ink)" stroke-width="1.5"/></svg>
    </div>
  </article>

  <!-- Concept two: dark brand panel, light contact panel -->
  <article class="card card--two">
    <svg class="card__shapes" viewBox="0 0 575 330" aria-hidden="true">
      <rect width="575" height="330" fill="var(--ink)"/>
      <rect width="30" height="330" fill="var(--paper)"/>
      <rect x="30" width="218" height="330" fill="var(--ink-soft)"/>
      <path d="M478 0 H512 V200 Q510 312 330 330 H478 Z" fill="var(--green)"/>
      <path d="M248 0 H496 V190 Q496 300 350 330 H248 Z" fill="var(--paper-shade)"/>
    </svg>
    <div class="brand" style="left:35px">
      <span class="brand__mark"></span>
      <span class="brand__name">KRWM</span>
    </div>
    <ul class="regions" style="left:262px">
      <li>Victoria</li><li>New South Wales</li><li>Queensland</li><li>Tasmania</li>
    </ul>
    <p class="email" style="left:262px"><span class="email__at">@</span>alex@krwm.com.au</p>
    <div class="web" style="left:513px">
      <span class="web__url">www.krwm.com.au</span>
      <svg class="web__icon" viewBox="0 0 16 16"><circle cx="8" cy="8" r="7" fill="none" stroke="#ffffff" stroke-width="2"/><path d="M1 8 H15 M8 1 V15" stroke="#ffffff" stroke-width="1.5"/></svg>
    </div>
  </article>

  <!-- Concept three: light brand panel, dark contact panel, green edge strip -->
  <article class="card card--three">
    <svg class="card__shapes" viewBox="0 0 575 330" aria-hidden="true">
      <rect width="575" height="330" fill="var(--green-bright)"/>
      <rect width="30" height="330" fill="var(--ink-soft)"/>
      <rect x="30" width="218" height="330" fill="var(--paper)"/>
      <path d="M470 0 H500 V200 Q498 312 330 330 H470 Z" fill="#ffffff"/>
      <path d="M248 0 H482 V190 Q482 300 350 330 H248 Z" fill="var(--ink)"/>
    </svg>
    <div class="brand" style="left:35px">
      <span class="brand__mark"></span>
      <span class="brand__name">KRWM</span>
    </div>
    <ul class="regions" style="left:262px">
      <li>Victoria</li><li>New South Wales</li><li>Queensland</li><li>Tasmania</li>
    </ul>
    <p class="email" style="left:260px"><span class="email__at">@</span>alex@krwm.com.au</p>
    <div class="web" style="left:508px">
      <span class="web__url">www.krwm.com.au</span>
      <svg class="web__icon" viewBox="0 0 16 16"><circle cx="8" cy="8" r="7" fill="none" stroke="var(--ink)" stroke-width="2"/><path d="M1 8 H15 M8 1 V15" stroke="var(--ink)" stroke-width="1.5"/></svg>
    </div>
  </article>

</main>
</body>
</html>
```